International Dental Education Website

This project is for a small teaching center on endodontic and micro dentistry in Norway. We need a Wordpress website design to display and highlight dental educational courses. Please use our new logo - see attached file. We like lighter, pastel oriented colors. The following sites are nicely laid out and you can use these as a guideline of sorts but I do want a unique site.
http://vorelta.nl/en, http://www.trasmolin.com/Education.aspx?currentSection=courses&cid=14,
http://www.kapiverno.com/.
Please create a space for a possible video on the home page. Please include a small contact form on the home page(name, email, phone, text box). Would like a horizonatal naviagtion bar. Would like an image to go across the whole top part of the site and this may rotate. Please use a stock image that shows a classroom type setting. Put phone number at the top of the screen. Put address and sitemap in a footer.

Reason: Upcoming vacation with limited internet access. Please continue to submit any designs. Thanks you.

Reason: The client is from a foreign country and is on an extended vacation.

Target Market(s)

General dentists (GPs) and specialists in Endodontics

Industry/Entity Type

Dental

Requirements
Must have
• Sitemap: HOME, COURSES, LECTURER, CONTACT US,
NORWEGIAN/ENGLISH. Phone number is: +47 93516072. Business name and address: Vatu Lok AS, Endodontic Teaching Center,
Solbergs vei 14C, 0291 Oslo, Norway.

```html
<!DOCTYPE html>
<html lang="en">
<head>
<meta charset="utf-8">
<title>Vatu Lok – Endodontic Teaching Center</title>
<link rel="stylesheet" href="https://fonts.googleapis.com/css2?family=Arimo:wght@400;700&family=Cabin:wght@400;600&family=Roboto+Slab:wght@700&display=swap">
<style>
:root{
  --teal:#5cc4cb;
  --teal-text:#4fb3bb;
  --pink:#e95bc8;
  --pink-dark:#c93ba8;
  --green:#5d9a1c;
  --ink:#2b2b2b;
  --body:#5e5e5e;
  --muted:#8a8a8a;
  --line:#dcdcdc;
  --panel:#f2f3f4;
  --panel-blue:#e4ebee;
  --tweet-blue:#2a9fd6;
  --footer-head:#5fd6ea;
  --white:#ffffff;
}
*{box-sizing:border-box;margin:0;padding:0}
html,body{width:909px;height:1200px;overflow:hidden}
body{position:relative;font-family:"Cabin",Arial,sans-serif;color:var(--body);
  background:linear-gradient(180deg,#eceff1 0,#f7f8f9 80px,#ffffff 400px,#ffffff 100%)}
.abs{position:absolute}
ul{list-style:none}
.nw{white-space:nowrap}

/* header */
.brand{left:128px;top:20px;font:700 26px/1 "Arimo",sans-serif;color:var(--teal-text)}
.brand-mark{display:inline-block;width:10px;height:10px;border-radius:50%;background:var(--teal-text);margin-left:4px;vertical-align:middle}
.call{right:279px;top:34px;display:flex;align-items:center;gap:4px;font-family:"Arimo",sans-serif;color:var(--ink);white-space:nowrap}
.call-label{font-size:13px}
.call-number{font-size:17px;margin-left:5px}
.lang{left:642px;top:22px;font:12px "Arimo",sans-serif;color:var(--ink)}
.lang-select{margin-top:3px;width:64px;height:19px;border:1px solid #9fc9cf;background:#fff;font-size:10px;padding:3px 4px;position:relative}
.lang-select::after{content:"";position:absolute;right:0;top:0;width:15px;height:17px;background:var(--teal)}
.lang-select svg{position:absolute;right:3px;top:6px;z-index:1}
.find{left:721px;top:22px;font:12px "Arimo",sans-serif;color:var(--ink)}
.social{display:flex;gap:4px;margin-top:3px}
.social span{width:20px;height:20px;border-radius:3px;background:#3b5b8f}
.social span:nth-child(2){background:#5fb7e5}
.social span:nth-child(3){background:#3a3a3a}

/* nav */
.nav{left:121px;top:81px;width:667px;height:36px;border-radius:4px 4px 0 0;
  background:linear-gradient(180deg,#86d6da,#55bcc4)}
.nav a{font:700 13px/36px "Arimo",sans-serif;color:#fff;text-decoration:none;position:absolute;top:0}
.nav .active{left:0;width:77px;background:linear-gradient(180deg,#5e8d9a,#466f7b);border-radius:4px 0 0 0;text-align:center}
.search{position:absolute;left:484px;top:6px;width:160px;height:22px;border-radius:3px;background:linear-gradient(180deg,#fff,#e8e8e8);
  font-size:9px;color:var(--ink);padding:5px 7px}
.search svg{position:absolute;right:6px;top:4px}

/* slider */
.slider{left:121px;top:117px;width:667px;height:274px;background:#fff;border:1px solid var(--line);border-top:0;border-radius:0 0 4px 4px}
.slide-photo{position:absolute;left:6px;top:8px;width:653px;height:258px;
  background:linear-gradient(100deg,#6a8a5c 0,#c05b9a 30%,#9fa6b5 55%,#7fa8cf 80%,#b7c9d9 100%)}
.slide-arrow{position:absolute;top:126px;width:22px;height:22px;border-radius:50%;background:#fff;box-shadow:0 1px 3px rgba(0,0,0,.3);display:flex;align-items:center;justify-content:center}
.caption{position:absolute;left:358px;top:203px;width:294px;height:41px;background:rgba(40,48,56,.82);
  font:700 22px/41px "Roboto Slab",serif;color:#fff;text-align:center;white-space:nowrap}
.dots{position:absolute;left:613px;top:252px;display:flex;gap:3px}
.dots i{width:5px;height:5px;border-radius:50%;background:#334}
.dots i:nth-child(2){background:var(--teal)}

/* upcoming */
.upcoming{left:121px;top:412px;width:204px}
.section-bar{height:25px;background:var(--pink);border-left:3px solid var(--pink-dark);color:#fff;font:15px/25px "Arimo",sans-serif;padding-left:9px}
.course{margin:10px 14px 0 22px;border-bottom:1px dotted #c9c9a0;height:48px;position:relative;white-space:nowrap}
.course::before{content:"";position:absolute;left:-10px;top:6px;width:3px;height:3px;background:#666}
.course h3{font:400 10.5px/14px "Cabin",sans-serif;color:var(--ink)}
.course p{font-size:9.3px;line-height:14px}
.course:last-of-type{border:0}
.readmore{font-size:10.5px;color:var(--green);white-space:nowrap}
.upcoming .readmore{text-align:right;padding:3px 7px 6px 0;border-bottom:1px solid var(--line)}

/* tweets */
.tweets{left:121px;top:710px;width:204px;height:240px;background:var(--panel);padding:12px 14px 0 14px}
.tweets h2{font:400 16px/19px "Arimo",sans-serif;color:var(--tweet-blue);margin-bottom:14px}
.tweet-badge{position:absolute;right:17px;top:3px;width:30px;height:30px;border-radius:50%;background:#4aa7e0}
.tweet{font-size:9.2px;line-height:13px;color:var(--body);margin-bottom:11px;white-space:nowrap}
.tweet b{font-weight:400;color:var(--tweet-blue)}
.tweet small{display:block;font-size:7.8px;line-height:11px;color:var(--muted)}

/* cards */
.card{background:#fff;border:1px solid var(--line);border-radius:4px}
.card h2,.comm h2{font:400 15px/18px "Arimo",sans-serif;color:var(--ink);padding-bottom:8px;border-bottom:1px dotted var(--line);margin-bottom:10px}

/* video */
.video-card{left:347px;top:413px;width:442px;height:221px;padding:12px 14px}
.video{position:absolute;left:14px;top:44px;width:216px;height:162px;background:linear-gradient(135deg,#5a5550,#8b7f6e 50%,#3d3a36)}
.play{position:absolute;left:94px;top:62px;width:28px;height:20px;border-radius:3px;background:rgba(255,255,255,.85)}
.play::after{content:"";position:absolute;left:11px;top:5px;border-left:8px solid #333;border-top:5px solid transparent;border-bottom:5px solid transparent}
.video-bar{position:absolute;left:0;bottom:0;width:100%;height:14px;background:#161616}
.video-bar::before{content:"";position:absolute;left:0;top:0;width:22px;height:2px;background:#d22}
.video-text{position:absolute;left:239px;top:42px;width:196px;font-size:9.2px;line-height:13px;white-space:nowrap}
.video-text .lead{font-size:10.5px;line-height:14.5px;color:var(--ink);font-weight:600;margin-bottom:9px}
.video-text p{margin-bottom:9px}

/* communication */
.comm{left:347px;top:655px;width:209px;height:296px;background:var(--panel-blue);border-radius:4px;padding:12px 14px}
.comm h2{border-bottom:1px solid #d1dbe0;margin-bottom:14px}
.comm-photo{width:181px;height:107px;background:linear-gradient(160deg,#e9eef2,#9fb3c4 60%,#4b5564)}
.comm p{font-size:9.2px;line-height:13px;margin-top:11px;white-space:nowrap}
.comm .readmore{position:absolute;right:14px;top:272px}

/* contact */
.contact{left:578px;top:655px;width:211px;height:296px;padding:12px 14px}
.field{width:181px;height:24px;border:1px solid #aaa;border-radius:2px;background:linear-gradient(180deg,#fff,#e6e6e6);font-size:9.5px;color:var(--ink);padding:5px 5px;margin-bottom:14px}
.field.area{height:80px}
.btn{width:60px;height:23px;border:1px solid #888;border-radius:3px;background:linear-gradient(180deg,#e8e8e8,#b5b5b5);font:11px/21px "Arimo",sans-serif;color:var(--ink);text-align:center}

/* footer */
.footer{left:0;top:975px;width:909px;height:225px;background:linear-gradient(180deg,#6b8a9b,#5a7888);box-shadow:inset 0 4px 6px rgba(0,0,0,.15)}
.footer h3{font:400 14px/18px "Cabin",sans-serif;color:var(--footer-head);margin-bottom:9px}
.footer p,.footer li{font-size:9.5px;line-height:14px;color:#fff;white-space:nowrap}
.fcol{position:absolute;top:18px}
.fcol li{font-size:10px;line-height:17px;padding-left:10px;position:relative}
.fcol li::before{content:"";position:absolute;left:0;top:7px;width:3px;height:3px;background:#fff}
.news-input{width:164px;height:20px;background:#fff;border:1px solid #999;font-size:9px;color:var(--ink);padding:4px 5px;margin-top:7px}
.footer .btn{margin-top:8px}
.footer .phone{font-size:10px;color:#fff;margin-top:6px}
.phone span{font:16px "Arimo",sans-serif}
.map{position:absolute;left:596px;top:103px;width:193px;height:100px;border-radius:5px;background:linear-gradient(135deg,#c9dcc0,#a9c7a2 50%,#b7d3e6)}
.footer .copy{position:absolute;left:121px;top:170px;font-size:9px;color:#e6eef2}
.fsocial{position:absolute;left:121px;top:189px;display:flex;gap:8px}
.fsocial span{width:18px;height:18px;border-radius:3px;background:#3f4d55}
</style>
</head>
<body>

<header>
  <div class="abs brand">Vatu Lok<span class="brand-mark"></span></div>
  <div class="abs call">
    <svg width="20" height="22" viewBox="0 0 20 22" aria-hidden="true"><path d="M6 2 L10 5 L8 9 C9 12 11 14 13 15 L16 13 L19 17 L16 20 C9 19 3 12 3 5 Z" fill="#5f8f99"/></svg>
    <span class="call-label">CALL US NOW!</span><span class="call-number">+47 93516072</span>
  </div>
  <div class="abs lang">Language:
    <div class="lang-select">English<svg width="8" height="5" viewBox="0 0 8 5"><path d="M0 0 H8 L4 5Z" fill="#fff"/></svg></div>
  </div>
  <div class="abs find">Find Us!
    <div class="social" aria-label="Social links"><span></span><span></span><span></span></div>
  </div>
</header>

<nav class="abs nav">
  <a class="active" href="#">HOME</a>
  <a href="#" style="left:113px">COURSES</a>
  <a href="#" style="left:211px">LECTURER</a>
  <a href="#" style="left:315px">CONTACT US</a>
  <div class="search">Search...
    <svg width="13" height="13" viewBox="0 0 13 13"><circle cx="5.5" cy="5.5" r="4" fill="none" stroke="#333" stroke-width="1.6"/><path d="M8.5 8.5 L12 12" stroke="#333" stroke-width="1.8"/></svg>
  </div>
</nav>

<section class="abs slider">
  <div class="slide-photo" role="img" aria-label="Smiling students studying outdoors with a laptop"></div>
  <div class="slide-arrow" style="left:1px"><svg width="8" height="10" viewBox="0 0 8 10"><path d="M6 0 L1 5 L6 10" fill="none" stroke="#333" stroke-width="2"/></svg></div>
  <div class="slide-arrow" style="left:642px"><svg width="8" height="10" viewBox="0 0 8 10"><path d="M2 0 L7 5 L2 10" fill="none" stroke="#333" stroke-width="2"/></svg></div>
  <div class="caption">We Develop knowledge...</div>
  <div class="dots"><i></i><i></i><i></i><i></i><i></i></div>
</section>

<aside class="abs upcoming">
  <div class="section-bar">Upcoming Courses</div>
  <div class="course"><h3>Name of the Courses</h3><p>Lorem Ipsum is simpl dummy into printing<br>industry the industry's text.</p></div>
  <div class="course"><h3>Name of the Courses</h3><p>Lorem Ipsum is simpl dummy into printing<br>industry the industry's text.</p></div>
  <div class="course"><h3>Name of the Courses</h3><p>Lorem Ipsum is simpl dummy into printing<br>industry the industry's text.</p></div>
  <div class="course"><h3>Name of the Courses</h3><p>Lorem Ipsum is simpl dummy into printing<br>industry the industry's text.</p></div>
  <div class="readmore">Read more ›</div>
</aside>

<aside class="abs tweets">
  <h2>Latest Tweets</h2>
  <span class="tweet-badge"></span>
  <div class="tweet"><b>@Lorem Ipsum</b> is simpl dummy into printing<br>industry the industry's aliquet at quis.<small>2 hours ago</small></div>
  <div class="tweet"><b>@Lorem Ipsum</b> is simpl dummy into printing<br>industry the industry's aliquet at quis.<small>2 hours ago</small></div>
  <div class="tweet"><b>@Lorem Ipsum</b> is simpl dummy into printing<br>industry the industry's aliquet at quis.<small>2 hours ago</small></div>
  <div class="tweet"><b>@Lorem Ipsum</b> is simpl dummy into printing<br>industry the industry's aliquet at quis.<small>2 hours ago</small></div>
</aside>

<section class="abs card video-card">
  <h2>Nurses Love yes! Nurses...</h2>
  <div class="video" role="img" aria-label="Video of a lecturer presenting at a flip chart to a seated class">
    <span class="play"></span><span class="video-bar"></span>
  </div>
  <div class="video-text">
    <p class="lead">Lorem Ipsum is simply dummy text of<br>the printing and simply dummy text of<br>typesetting industry.</p>
    <p>Lorem Ipsum is dummy text of the printing and<br>typesetting industry. Lorem Ipsum since to<br>and typesetting indus of Ipsum has the indus-<br>try's standard dummy text ever since.</p>
    <p>Lorem Ipsum since to and typesetting indus of<br>the industry's standard.</p>
    <div class="readmore">Read more ›</div>
  </div>
</section>

<section class="abs comm">
  <h2>Communication</h2>
  <div class="comm-photo" role="img" aria-label="Colleagues shaking hands across a meeting table"></div>
  <p>Lorem Ipsum is dummy text of the printing<br>and typesetting industry. Lorem Ipsum since<br>been the industry's standard dummy text<br>ever since.<br>Dummy text of the printing and typesetting<br>industry the printing and typesetting lorem<br>Ipsum the printing and typesetting.</p>
  <div class="readmore">Read more ›</div>
</section>

<section class="abs card contact">
  <h2>Quick Contact</h2>
  <div class="field" style="margin-top:13px">Enter your name:</div>
  <div class="field">Enter your email:</div>
  <div class="field">Phone:</div>
  <div class="field area">Massage:</div>
  <div class="btn">SUBMIT</div>
</section>

<footer class="abs footer">
  <div class="fcol" style="left:121px;width:175px">
    <h3>News Letter</h3>
    <p>Lorem Ipsum is simpl dummy into printing<br>industry the industry's text</p>
    <p style="font-size:10.5px;margin-top:7px">Sign up to our Newsletter!</p>
    <div class="news-input">Enter your email...</div>
    <div class="btn">SUBMIT</div>
  </div>
  <div class="fcol" style="left:311px">
    <h3>Our Cources</h3>
    <ul><li>Lorem Ipsum is simply</li><li>including versions</li><li>industry's standard dummy</li><li>popularised</li><li>including versions</li></ul>
  </div>
  <div class="fcol" style="left:473px">
    <h3>Our Cources</h3>
    <ul><li>Home</li><li>Courses</li><li>Lectuere</li><li>Contact Us</li></ul>
  </div>
  <div class="fcol" style="left:597px;width:200px">
    <h3>Contact Us</h3>
    <p style="font-size:10px">Vatu Lok AS, Endodontic Teaching Center,<br>Solbergs vei 14C, 0291 Oslo, Norway.</p>
    <p class="phone">Phone: <span>+47 93516072</span></p>
  </div>
  <div class="map" role="img" aria-label="Map showing the teaching center location"></div>
  <p class="copy">Copyright © 2012 Dental Education. All Rights Reserved.</p>
  <div class="fsocial" aria-label="Social links"><span></span><span></span><span></span><span></span></div>
</footer>

</body>
</html>
```